Life Coach for Lawyers Business Card Design

Elegant, original, business card design for life coaching service for associate attorneys who work in big law and struggle with stress, overwhelm, and time management. Double sided design.

Target Market(s)

Women associate attorneys who work in big law and struggle with stress, overwhelm, and time management.

Industry/Entity Type

Life Coaching

Contact Information for Business Card

Marissa Pendrell
Life Coach
518.677.3941
calmbriefcounsel.net
marissa@calmbriefcounsel.net
@calmbriefcounsel (Instagram)

Font styles to use
Other font styles liked:
• Silver South font duo. See uploaded files.

Requirements
Must have
• Icons for phone, website, email, and Instagram instead of words. Specific colors used in my logo (171B2B, 421121, FFFFFF)
Nice to have
• Foil. Embossed. Feminine design.
Should not have
• Any colors other than those used in logo. See uploaded files.

```html
<!DOCTYPE html>
<html lang="en">
<head>
<meta charset="utf-8">
<title>Calm Brief Counsel – Business Card</title>
<link rel="stylesheet" href="https://fonts.googleapis.com/css2?family=Bodoni+Moda:wght@400&family=Allura&family=Cormorant+Garamond:wght@500&display=swap">
<style>
  :root {
    --navy: #2e3a5a;
    --maroon: #421121;
    --white: #ffffff;
    --ink: #2a2a2a;
    --faint: #e4e4e4;
    --backdrop: #eef0f3;
  }
  * { box-sizing: border-box; margin: 0; padding: 0; }
  html, body { width: 1200px; height: 1135px; overflow: hidden; background: var(--backdrop); }
  .sheet {
    width: 1200px; height: 1135px;
    display: flex; align-items: center; justify-content: center; gap: 60px;
  }
  .card {
    position: relative; width: 500px; height: 286px; overflow: hidden;
    box-shadow: 0 10px 24px rgba(0,0,0,.18);
  }
  .card--front { background: var(--white); }
  .card--back { background: var(--navy); display: flex; align-items: center; justify-content: center; }

  .front__ring {
    position: absolute; right: -70px; top: -40px; width: 250px; height: 250px;
    border: 2px solid var(--faint); border-radius: 50%;
  }
  .front__brand {
    position: absolute; top: 34px; left: 0; width: 100%; text-align: center;
    font-family: "Bodoni Moda", serif; font-weight: 400; font-size: 24px;
    color: var(--maroon); letter-spacing: .04em; text-transform: uppercase;
  }
  .front__name {
    position: absolute; top: 98px; left: 70px; width: 230px; text-align: center;
    font-family: "Allura", cursive; font-size: 32px; line-height: 44px; color: var(--maroon);
    white-space: nowrap;
  }
  .front__rule {
    position: absolute; top: 146px; left: 40px; width: 250px; height: 1px; background: var(--maroon);
  }
  .front__role {
    position: absolute; top: 152px; left: 70px; width: 230px; text-align: center;
    font-family: "Cormorant Garamond", serif; font-weight: 500; font-size: 13px;
    letter-spacing: .08em; color: var(--ink);
  }
  .contact {
    position: absolute; list-style: none;
    font-family: "Cormorant Garamond", serif; font-weight: 500; font-size: 11.5px; color: var(--ink);
    white-space: nowrap;
  }
  .contact li { display: flex; align-items: center; gap: 9px; height: 26px; }
  .contact svg { width: 15px; height: 15px; flex: none; }
  .contact--left { left: 40px; top: 200px; }
  .contact--right { left: 305px; top: 168px; }

  .back__badge {
    width: 190px; height: 190px; border: 1.5px solid var(--white); border-radius: 50%;
    display: flex; align-items: center; justify-content: center; text-align: center;
    font-family: "Bodoni Moda", serif; font-weight: 400; font-size: 19px; line-height: 1.35;
    color: var(--white); letter-spacing: .08em; text-transform: uppercase;
  }
</style>
</head>
<body>
<main class="sheet">
  <section class="card card--front" aria-label="Card front">
    <div class="front__ring"></div>
    <p class="front__brand">Calm Brief Counsel</p>
    <p class="front__name">Marissa Pendrell</p>
    <div class="front__rule"></div>
    <p class="front__role">LIFE COACH</p>

    <ul class="contact contact--right">
      <li>
        <svg viewBox="0 0 16 16" aria-hidden="true"><circle cx="8" cy="8" r="6.5" fill="none" stroke="var(--maroon)" stroke-width="1.4"/><circle cx="8" cy="8" r="2.5" fill="none" stroke="var(--maroon)" stroke-width="1.4"/></svg>
        marissa@calmbriefcounsel.net
      </li>
      <li>
        <svg viewBox="0 0 16 16" aria-hidden="true"><rect x="1.5" y="1.5" width="13" height="13" rx="3" fill="var(--maroon)"/></svg>
        @calmbriefcounsel
      </li>
    </ul>

    <ul class="contact contact--left">
      <li>
        <svg viewBox="0 0 16 16" aria-hidden="true"><rect x="4" y="1" width="8" height="14" rx="1.5" fill="none" stroke="var(--maroon)" stroke-width="1.3"/><line x1="7" y1="12.5" x2="9" y2="12.5" stroke="var(--maroon)" stroke-width="1.3"/></svg>
        518.677.3941
      </li>
      <li>
        <svg viewBox="0 0 16 16" aria-hidden="true"><circle cx="8" cy="8" r="7" fill="var(--maroon)"/><g fill="none" stroke="var(--white)" stroke-width=".9"><ellipse cx="8" cy="8" rx="3" ry="6"/><line x1="2" y1="8" x2="14" y2="8"/><line x1="8" y1="2" x2="8" y2="14"/></g></svg>
        calmbriefcounsel.net
      </li>
    </ul>
  </section>

  <section class="card card--back" aria-label="Card back">
    <div class="back__badge">Calm<br>Brief<br>Counsel</div>
  </section>
</main>
</body>
</html>
```